Tidewell Pronto Clinic Business card

We want a business card that matches our business theme. Our website is www.prontoclinicbz.example
The company name is Tidewell Pronto Clinic
The persons having the business cards will be doctors
My logo is attached.
We have a drive-thru medical center where our motto is Fast, Reliable, and Convenient. Our goal is to change the medical space while utilizing technologies, keeping a professional and clean look

Medical

Info on the card should be: Name, Position, Cell number, website, email address, possibly the office line as well

• Logo
• Professional medical feel with our logo colors incorporated

```html
<!DOCTYPE html>
<html lang="en">
<head>
<meta charset="utf-8">
<title>Tidewell Pronto Clinic – Business Card</title>
<link href="https://fonts.googleapis.com/css2?family=Montserrat:wght@600;800&family=Roboto:wght@400;500&display=swap" rel="stylesheet">
<style>
  :root {
    --stage: #262626;
    --deep-blue: #1b48a6;
    --mid-blue: #2f8fd8;
    --sky-blue: #3ec8f5;
    --white: #ffffff;
    --ink: #1a1a1a;
    --faint: #f2f2f2;
    --rule: #b5b5b5;
  }
  * { margin: 0; padding: 0; box-sizing: border-box; }
  html, body { width: 1200px; height: 1015px; overflow: hidden; }
  body {
    background: var(--stage);
    position: relative;
    font-family: "Montserrat", sans-serif;
  }
  .card {
    position: absolute;
    width: 560px;
    height: 320px;
    overflow: hidden;
    box-shadow: 0 18px 40px rgba(0,0,0,.55);
  }

  /* Front (blue) */
  .card--front {
    left: 80px; top: 140px;
    background: linear-gradient(200deg, var(--sky-blue) 0%, var(--mid-blue) 45%, var(--deep-blue) 100%);
  }
  .card--front .deco-circle {
    position: absolute;
    width: 300px; height: 300px;
    right: 40px; top: -10px;
    border-radius: 50%;
    background: rgba(27,72,166,.18);
  }
  .brand {
    position: absolute;
    display: flex;
    flex-direction: column;
  }
  .brand__row { display: flex; align-items: center; }
  .brand__band {
    padding: 8px 26px 8px 22px;
    font-weight: 800;
    font-size: 26px;
    line-height: 1.05;
  }
  .brand__dot {
    width: 62px; height: 62px;
    border-radius: 50%;
    margin-left: -14px;
  }
  .brand__tagline {
    margin-top: 8px;
    font-family: "Montserrat", sans-serif;
    font-weight: 600;
    font-size: 11px;
    letter-spacing: 1.4px;
  }
  .card--front .brand { left: 130px; top: 112px; }
  .card--front .brand__band { background: var(--white); color: var(--deep-blue); }
  .card--front .brand__dot { background: var(--white); }
  .card--front .brand__tagline { color: var(--white); }

  /* Back (white) */
  .card--back {
    left: 560px; top: 555px;
    background: var(--white);
    border-bottom: 3px solid var(--deep-blue);
  }
  .card--back .deco-circle {
    position: absolute;
    width: 290px; height: 290px;
    right: 40px; top: -20px;
    border-radius: 50%;
    background: var(--faint);
  }
  .card--back .brand { left: 34px; top: 92px; }
  .card--back .brand__band { background: var(--deep-blue); color: var(--white); font-size: 22px; }
  .card--back .brand__dot { background: var(--deep-blue); width: 54px; height: 54px; }
  .card--back .brand__tagline { color: var(--ink); font-size: 9.5px; }

  .divider {
    position: absolute;
    left: 300px; top: 60px;
    width: 1px; height: 150px;
    background: var(--rule);
  }
  .contact {
    position: absolute;
    left: 322px; top: 62px;
    font-family: "Roboto", sans-serif;
    color: var(--ink);
  }
  .contact__name {
    font-family: "Montserrat", sans-serif;
    font-weight: 800;
    font-size: 21px;
    color: var(--deep-blue);
  }
  .contact__role { font-size: 13px; margin-bottom: 12px; }
  .contact__line {
    display: flex; align-items: center; gap: 8px;
    font-size: 13.5px; line-height: 1.55;
  }
  .contact__line svg { width: 14px; height: 14px; flex: none; }

  .web-band {
    position: absolute;
    left: 150px; right: 30px; bottom: 34px;
    height: 36px;
    background: var(--deep-blue);
    color: var(--white);
    font-family: "Roboto", sans-serif;
    font-weight: 500;
    font-size: 15px;
    letter-spacing: 1.6px;
    display: flex; align-items: center;
    padding-left: 60px;
  }
  .web-band__dot {
    position: absolute;
    right: -6px; top: 50%;
    transform: translateY(-50%);
    width: 42px; height: 42px;
    border-radius: 50%;
    background: var(--white);
    border: 4px solid var(--deep-blue);
  }
</style>
</head>
<body>

<section class="card card--front" aria-label="Business card front">
  <div class="deco-circle"></div>
  <div class="brand">
    <div class="brand__row">
      <div class="brand__band">Tidewell<br>Pronto Clinic</div>
      <div class="brand__dot"></div>
    </div>
    <div class="brand__tagline">FAST I RELIABLE I CONVENIENT</div>
  </div>
</section>

<section class="card card--back" aria-label="Business card back">
  <div class="deco-circle"></div>

  <div class="brand">
    <div class="brand__row">
      <div class="brand__band">Tidewell<br>Pronto Clinic</div>
      <div class="brand__dot"></div>
    </div>
    <div class="brand__tagline">FAST I RELIABLE I CONVENIENT</div>
  </div>

  <div class="divider"></div>

  <div class="contact">
    <div class="contact__name">Marcus Ellery</div>
    <div class="contact__role">Managing Director</div>
    <div class="contact__line">
      <svg viewBox="0 0 24 24"><path fill="#1b48a6" d="M6.6 10.8a15 15 0 0 0 6.6 6.6l2.2-2.2c.3-.3.7-.4 1-.2 1.1.4 2.3.6 3.6.6.6 0 1 .4 1 1V20c0 .6-.4 1-1 1A17 17 0 0 1 3 4c0-.6.4-1 1-1h3.5c.6 0 1 .4 1 1 0 1.3.2 2.5.6 3.6.1.3 0 .7-.2 1z"/></svg>
      044-555 010 220
    </div>
    <div class="contact__line">
      <svg viewBox="0 0 24 24"><rect x="6" y="2" width="12" height="20" rx="2" fill="none" stroke="#1b48a6" stroke-width="2"/><circle cx="12" cy="18" r="1.2" fill="#1b48a6"/></svg>
      044-555 010 221
    </div>
    <div class="contact__line">
      <svg viewBox="0 0 24 24"><rect x="2" y="5" width="20" height="14" fill="#1b48a6"/><path d="M2 5l10 8 10-8" fill="none" stroke="#fff" stroke-width="1.6"/></svg>
      info@prontoclinic.example
    </div>
  </div>

  <div class="web-band">
    www.prontoclinicbz.example
    <span class="web-band__dot"></span>
  </div>
</section>

</body>
</html>
```